Design a Bold Tradeshow Backdrop for a Sustainable Cleaning Technology

We need a professional, high-impact 10' × 8' tradeshow backdrop for Vornelle®, a commercial cleaning technology company. 143.75" x 90" high and needs bleeds in the 143.75" direction for printing but the graphic area is 10' wide.

Our first event will have an audience that includes K–12 school administrators, facility managers, business officials, and custodial decision-makers. However, this backdrop will be used at multiple future trade shows across different commercial and institutional markets.

The design therefore needs to be universal rather than specifically education- or school-themed.

Our goal is to stop attendees as they walk past the booth and immediately communicate a simple message:

Safer and more sustainable cleaning can also cost substantially less than conventional cleaning chemicals.

We want the design to feel modern, innovative, clean, sustainable, credible, commercial, and premium. It should resonate with K–12 decision-makers while being equally appropriate at events serving commercial facilities, healthcare, hospitality, government, property management, transportation, and other institutional markets.

It should NOT look like a traditional janitorial supply advertisement and should not be overly busy.

The most important messages need to be understandable from approximately 10–20 feet away.

Required Messaging

The primary headline should be:

SUSTAINABLE CLEANING
DOES NOT HAVE TO BE EXPENSIVE.

Three major value propositions should be prominently displayed:

FREE
Cleaning Chemical Analysis
See how much you can save.

SAVE UP TO 60% or More
on Cleaning Chemical Costs

AS LITTLE AS $0.27/GALLON

We would also like a strong secondary message incorporated into the design:

SMARTER CLEANING.
High Performance. Low Cost. Safer.

Visual Direction — Important

Rather than showing a K–12 school hallway or other environment that limits the backdrop to the education market, we want a sophisticated, universal commercial or institutional environment.

This could be a bright, contemporary commercial facility, lobby, corridor, office environment, public building, or other premium architectural space that could reasonably represent many different types of facilities.

The environment should communicate:

Cleanliness • Safety • Sustainability • Professionalism • Efficiency • High Performance

We want someone from a school, hospital, hotel, office building, airport, government facility, or other commercial property to be able to look at the backdrop and relate the imagery to their own facility.

Please avoid imagery that makes the backdrop industry-specific.

We also want to avoid clichéd environmental imagery. The design does not need to be covered in leaves, trees, water droplets, recycling symbols, or other obvious "green" graphics to communicate sustainability. We prefer a sophisticated commercial interpretation of sustainability.

Color & Brand Direction

We want the overall color palette to stay primarily within:

Blues — consistent with our corporate identity

Greens — to reinforce sustainability, safety, efficiency, and environmental responsibility

White — strongly encouraged for clean space, contrast, and an open contemporary appearance

Black — should be limited primarily to text where necessary for readability

Please avoid making black a major background or dominant design color.

We want the finished display to have a bright, clean, sophisticated, sustainable look and feel rather than a dark or industrial appearance.

The design should use significant negative space and a strong visual hierarchy.

Less is more.

We prefer a few large, powerful messages that can be understood quickly rather than numerous small bullet points, paragraphs, or icons.

Creative Freedom

The attached concept image is provided to communicate our general direction and messaging only.

It does not need to be copied.

We are specifically running this contest because we want designers to improve upon our initial concept and show us different creative approaches to presenting the Vornelle value proposition.

We are open to creative interpretations of the commercial environment, composition, typography, use of negative space, and how the three major financial benefits are presented.

The finished design should feel like an innovative commercial technology brand, not simply another cleaning chemical company.

Corporate Logo — Very Important

We are attaching our official Vornelle® corporate logo for use in the design.

DO NOT redraw, recreate, modify, stylize, reinterpret, trace, or AI-generate the Vornelle logo.

The supplied corporate logo must be inserted directly into the artwork exactly as provided, maintaining its original proportions, colors, typography, trademark elements, and graphic design.

The logo should generally appear in the upper-left area of the backdrop but should not overwhelm the primary marketing message.

Printer Template & Graphic Sizing

We are also attaching the printer's official graphic template and instructions for the 8' × 8' tension-fabric display.

Designers should create their artwork using these supplied specifications so the winning design can be transferred directly into production.

The printer requires that the original document size not be changed, artwork be created on the designated design layer or a new layer, images be embedded, text be converted to outlines, and the finished production artwork be supplied as a PDF.

Please pay particular attention to the bleed area, finished size, and safe artwork area when positioning important text, graphics, and the corporate logo.

Physical Booth Context

The backdrop will sit behind an 8' tradeshow table.

The complete booth will also contain:

A blue stretch tablecloth with the Vornelle corporate logo
BrevoMax and Vornelle product containers and samples on the table
An HulaDrent chemical mixing/dilution station displayed on an elevated stand to the left
A television/monitor to the right demonstrating our online ROI cost-savings calculator

Because these other booth elements will explain our products and technology in greater detail, the backdrop should NOT attempt to explain everything we do.

Its primary purpose is to stop traffic, establish the Vornelle brand, and communicate our core economic and sustainability value proposition.

Final Deliverables

The winning designer must provide artwork properly sized and positioned using our supplied 8' × 8' tension-fabric display template.

Final files should include:

Print-ready, high-resolution PDF
Editable source/vector artwork
All images embedded
Fonts converted to outlines
Artwork correctly positioned within the supplied printer template
Original Vornelle corporate logo incorporated without modification
The 3–5 Second Test

This is perhaps the most important requirement.

Someone walking down a tradeshow aisle should be able to look at the backdrop for 3–5 seconds and understand:

Vornelle offers safer, sustainable, high-performance commercial cleaning — at a lower cost.

The three offers we particularly want them to remember are:

FREE CHEMICAL ANALYSIS

SAVE UP TO 60%

AS LITTLE AS $0.27/GALLON

The overall takeaway should be:

Sustainable cleaning does not have to cost more.

We want the winning design to make that message immediately understandable, credible, and memorable.

Colors
0054AA
0677BA
7BADD7
CADEEF
E8F1F8
0094D4
00A9DD
6FCCEA
C7EBF8
E9F6FB
00AB8E
00BBA5
67D7C9
C6EFE9
E9F9F6
59FF00
82FF00
B8FF75
E3FFCB
F4FFEA

```html
<!DOCTYPE html>
<html lang="en">
<head>
<meta charset="utf-8">
<title>Vornelle Tension Fabric Backdrop – Artwork Template</title>
<link rel="stylesheet" href="https://fonts.googleapis.com/css2?family=Poppins:wght@400;500;700;800;900&family=Source+Sans+3:wght@400;600&family=Arimo:wght@400;700&display=swap">
<style>
  :root{
    --navy:#14254f;
    --brand-blue:#0054AA;
    --sky:#0094D4;
    --leaf:#6fa53c;
    --gold:#f5c400;
    --white:#ffffff;
    --ink:#111111;
    --alert:#e3141b;
    --bleed:#8f8f94;
    --finished:#00a9e8;
    --safe:#4cbf45;
    --glass-1:#eef2f5;
    --glass-2:#c9d3da;
  }
  *{box-sizing:border-box;margin:0;padding:0}
  html,body{width:1200px;height:612px;overflow:hidden;background:var(--white)}
  .canvas{position:relative;width:1200px;height:612px;background:var(--white);font-family:"Poppins",sans-serif}
  .artboard-graphics{position:absolute;left:0;top:0}
  .abs{position:absolute;white-space:nowrap}

  .brand{left:204px;top:80px;display:flex;align-items:center;gap:7px}
  .brand-mark{width:16px;height:16px;background:var(--gold)}
  .brand-name{font-family:"Poppins",sans-serif;font-weight:700;font-size:28px;color:var(--navy);line-height:1}
  .brand-tagline{left:204px;top:131px;font-family:"Source Sans 3",sans-serif;font-weight:600;font-size:11.5px;letter-spacing:1.6px;color:var(--navy)}

  .headline{left:204px;font-weight:900;font-size:37px;line-height:1;color:var(--navy);transform:scaleX(.96);transform-origin:left top;letter-spacing:-.3px}
  .headline--one{top:156px}
  .headline--two{top:187px}
  .headline--accent{top:245px;color:var(--leaf)}
  .headline-sub{left:205px;top:220px;font-family:"Source Sans 3",sans-serif;font-weight:400;font-size:24px;line-height:1;color:var(--ink);transform:scaleX(.98);transform-origin:left top}

  .offer{top:300px;width:80px;text-align:center;color:var(--navy)}
  .offer--analysis{left:199px}
  .offer--save{left:284px}
  .offer--price{left:354px}
  .offer-icon{display:block;margin:0 auto;height:38px}
  .offer-title{font-weight:800;font-size:14px;line-height:1;margin-top:8px}
  .offer-note{font-size:6.6px;line-height:1.2;font-weight:400}
  .offer-note strong{font-weight:800}
  .offer-dollar{font-weight:700;font-size:44px;line-height:38px;height:38px}
  .offer-small{font-weight:800;font-size:6.2px;line-height:1.25}
  .offer-price{font-weight:800;font-size:16px;line-height:1}
  .offer-divider{top:302px;width:1px;height:80px;background:var(--navy)}

  .band-title{left:205px;top:440px;font-weight:800;font-size:22.5px;line-height:1;color:var(--white);letter-spacing:-.2px}
  .band-sub{left:205px;top:465px;font-weight:400;font-size:14.3px;line-height:1;color:var(--white)}

  .template-panel{position:absolute;left:768px;top:45px;width:288px;height:373px;border:1px solid #333;font-family:"Arimo",sans-serif;color:var(--ink)}
  .panel-title{position:absolute;left:15px;top:13px;font-weight:700;font-size:25.5px;line-height:25px;white-space:nowrap}
  .panel-subtitle{position:absolute;left:15px;top:64px;font-weight:700;font-size:15px;white-space:nowrap}
  .panel-alert{position:absolute;left:18px;top:106px;font-size:12px;line-height:17.6px;color:var(--alert);white-space:nowrap}
  .panel-steps{position:absolute;left:18px;top:175px;font-size:12px;line-height:17.5px;list-style:none;white-space:nowrap}
  .panel-steps .indent{padding-left:14px}
  .panel-steps .indent-more{padding-left:17px}
  .legend{position:absolute;left:154px;top:328px;font-size:10.5px;line-height:12px}
  .legend-row{display:flex;align-items:center;gap:7px;margin-bottom:0.2px}
  .legend-swatch{width:26px;height:10px}
  .legend--bleed .legend-swatch{background:var(--bleed)} .legend--bleed{color:var(--bleed)}
  .legend--finished .legend-swatch{background:var(--finished)} .legend--finished{color:var(--finished)}
  .legend--safe .legend-swatch{background:var(--safe)} .legend--safe{color:var(--safe)}
</style>
</head>
<body>
<div class="canvas">

  <svg class="artboard-graphics" width="1200" height="612" viewBox="0 0 1200 612">
    <defs>
      <clipPath id="artboard-clip">
        <path d="M176,570 V74 Q176,46 204,46 H671 Q699,46 699,74 V570 Z"/>
      </clipPath>
      <linearGradient id="glass-tone" x1="0" y1="0" x2="0.4" y2="1">
        <stop offset="0" stop-color="#dfe5ea"/>
        <stop offset="0.45" stop-color="var(--glass-1)"/>
        <stop offset="1" stop-color="var(--glass-2)"/>
      </linearGradient>
    </defs>
    <g clip-path="url(#artboard-clip)">
      <rect x="176" y="46" width="523" height="524" fill="var(--white)"/>
      <path class="lobby-photo" role="img" aria-label="Bright modern office lounge with glass walls, white sofa, coffee table and city view"
            d="M680,60 Q420,160 438,338 Q452,500 586,570 L699,570 L699,60 Z" fill="url(#glass-tone)"/>
      <path class="swoosh-top" d="M699,46 C560,52 458,140 440,277 C492,156 592,88 699,80 Z" fill="var(--leaf)"/>
      <path class="swoosh-upper" d="M176,375 Q236,426 320,431 Q236,424 176,398 Z" fill="var(--leaf)"/>
      <path class="message-band" d="M176,396 Q320,462 436,396 L495,511 Q330,468 176,544 Z" fill="var(--brand-blue)"/>
      <path class="swoosh-lower" d="M176,570 Q244,500 356,490 Q252,508 176,548 Z" fill="var(--leaf)"/>
    </g>
    <path class="line-bleed" d="M176,570 V74 Q176,46 204,46 H671 Q699,46 699,74 V570 Z" fill="none" stroke="var(--bleed)" stroke-width="0.8"/>
    <path class="line-finished" d="M183,563 V80 Q183,53 210,53 H665 Q692,53 692,80 V563 Z" fill="none" stroke="var(--finished)" stroke-width="0.8"/>
    <path class="line-safe" d="M189,557 V86 Q189,59 216,59 H659 Q686,59 686,86 V557 Z" fill="none" stroke="var(--safe)" stroke-width="0.8"/>
  </svg>

  <div class="abs brand"><span class="brand-mark"></span><span class="brand-name">Vornelle®</span></div>
  <div class="abs brand-tagline">CLEAN ASSURE™</div>

  <h1>
    <span class="abs headline headline--one">SUSTAINABLE</span>
    <span class="abs headline headline--two">CLEANING</span>
    <span class="abs headline-sub">DOES NOT HAVE TO BE</span>
    <span class="abs headline headline--accent">EXPENSIVE.</span>
  </h1>

  <div class="abs offer offer--analysis">
    <svg class="offer-icon" viewBox="0 0 30 38" width="30" height="38">
      <path d="M11,2 H19 M12,2 V13 L3,32 Q2,36 6,36 H24 Q28,36 27,32 L18,13 V2" fill="none" stroke="var(--navy)" stroke-width="2.2" stroke-linejoin="round"/>
      <path d="M7,24 H23 L26.5,32 Q27,34.5 24,34.5 H6 Q3,34.5 3.5,32 Z" fill="var(--navy)"/>
    </svg>
    <div class="offer-title">FREE</div>
    <div class="offer-note">Cleaning Chemical<br>Analysis (See how<br>much you can save.)</div>
  </div>
  <div class="abs offer-divider" style="left:287px"></div>

  <div class="abs offer offer--save">
    <svg class="offer-icon" viewBox="0 0 36 38" width="36" height="38">
      <path d="M2,2 V35 H35" fill="none" stroke="var(--navy)" stroke-width="2.6"/>
      <rect x="8" y="27" width="3" height="6" fill="var(--navy)"/>
      <rect x="14" y="23" width="3" height="10" fill="var(--navy)"/>
      <rect x="20" y="19" width="3" height="14" fill="var(--navy)"/>
      <rect x="26" y="15" width="3" height="18" fill="var(--navy)"/>
      <path d="M7,22 L16,14 L21,17 L31,7" fill="none" stroke="var(--navy)" stroke-width="2.2"/>
      <path d="M25,5 H33 V13 Z" fill="var(--navy)"/>
    </svg>
    <div class="offer-title">SAVE</div>
    <div class="offer-note"><strong>UP TO 60%</strong><br>on Cleaning<br>Chemical Costs</div>
  </div>
  <div class="abs offer-divider" style="left:362px"></div>

  <div class="abs offer offer--price">
    <div class="offer-dollar">$</div>
    <div class="offer-small" style="margin-top:7px">AS LITTLE<br>AS</div>
    <div class="offer-price">$0.27/</div>
    <div class="offer-small">GALLON</div>
  </div>

  <div class="abs band-title">SMARTER CLEANING.</div>
  <div class="abs band-sub">High Performance. Low Cost. Safer.</div>

  <aside class="template-panel">
    <div class="panel-title">Tension Fabric Display<br>Straight 8Ft x 8Ft</div>
    <div class="panel-subtitle">Artwork Template</div>
    <p class="panel-alert">IMPORTANT INFORMATION<br>(Failure to follow these instructions will<br>slow the automatic processing of your job)</p>
    <ol class="panel-steps">
      <li>1. Do not modify the document size of this file.</li>
      <li>2. Do not edit or remove locked layers.</li>
      <li>3. Create your artwork on the ‘Your Design’ layer</li>
      <li class="indent">or on your own new layer.</li>
      <li>4. Once your design is complete, ensure you</li>
      <li class="indent-more">convert all text to outlines &amp; embed images.</li>
      <li>5. Save this file as a PDF and upload on</li>
      <li class="indent-more">our file upload page after checking out.</li>
    </ol>
    <div class="legend">
      <div class="legend-row legend--bleed"><span class="legend-swatch"></span>Bleed Area</div>
      <div class="legend-row legend--finished"><span class="legend-swatch"></span>Finished Size</div>
      <div class="legend-row legend--safe"><span class="legend-swatch"></span>Safe Artwork Area</div>
    </div>
  </aside>

</div>
</body>
</html>
```